Get Up to $ 500,000 in Business Capital within 48 hours

design a flyer offering business capital to businesses. The flyer is going to be mailed to business owners and the flyer needs to immediately capture their attention.
The flyer needs to be bold and professional and really stand-out.
pppppppppppppppppppppppppppppppppppppppppppppppppppppppppppppppppppppppppppppppppppppppppppppppppppppppppppppppppppppppppppppppppppppppppppppppppppppppppppppppppppppppppppppppppppppppppppppppppppppppppppppppppppppppppppppppppppppp

Target Market(s)

business owners

Font styles to use
Serif

Requirements
Must have
• Apply online in minutes at PellarCapital.example or call 800-GRAB-NOW
Nice to have
• We fund almost every business type. Not a business loan, receive a cash advance on your future sales.

```html
<!DOCTYPE html>
<html lang="en">
<head>
<meta charset="utf-8">
<title>PellarCapital – Business Capital Flyer</title>
<link rel="stylesheet" href="https://fonts.googleapis.com/css2?family=Oswald:wght@500;600&family=Roboto:wght@400;500;700&display=swap">
<style>
  :root {
    --backdrop: #2a2a2a;
    --paper: #ffffff;
    --navy: #1f2f7c;
    --ink: #1d2a6b;
    --brand-blue: #1c5fae;
    --sky: #2ea3e8;
    --band-start: #1a8fd6;
    --band-end: #8fa3c2;
    --gold: #f5c12e;
  }
  * { box-sizing: border-box; margin: 0; padding: 0; }
  html, body { width: 1200px; height: 1200px; overflow: hidden; }
  body { background: var(--backdrop); font-family: "Roboto", Arial, sans-serif; position: relative; }

  .flyer {
    position: absolute; left: 234px; top: 82px;
    width: 732px; height: 1036px;
    background: var(--paper); overflow: hidden;
  }
  .hero-photo {
    position: absolute; left: 0; top: 0; width: 732px; height: 456px;
    background:
      radial-gradient(circle at 20% 55%, rgba(245,190,60,0.75) 0, rgba(245,190,60,0) 28%),
      radial-gradient(circle at 70% 35%, rgba(220,225,235,0.6) 0, rgba(220,225,235,0) 30%),
      linear-gradient(120deg, #6f7f96 0%, #9aa6b6 40%, #4d5f7a 75%, #34455f 100%);
  }
  .logo-band { position: absolute; left: 0; top: 0; width: 444px; height: 96px; }
  .logo {
    position: absolute; left: 24px; top: 14px;
    font-family: "Roboto", Arial, sans-serif; font-weight: 500;
    font-size: 46px; line-height: 56px; letter-spacing: 0.5px; color: var(--brand-blue);
  }

  .headline-band {
    position: absolute; left: 0; top: 464px; width: 732px; height: 104px;
    background: linear-gradient(90deg, var(--band-start) 0%, #2f6fb4 55%, var(--band-end) 100%);
  }
  .headline-band::before {
    content: ""; position: absolute; left: 2px; top: 14px; width: 7px; height: 76px; background: var(--gold);
  }
  .headline {
    position: absolute; left: 24px; top: 0; height: 104px;
    display: flex; align-items: center;
    font-family: "Oswald", "Arial Narrow", sans-serif; font-weight: 500;
    font-size: 50px; line-height: 1; color: #fff; letter-spacing: 0.2px;
  }

  .badge {
    position: absolute; left: 542px; top: 376px; width: 178px; height: 178px;
    border-radius: 50%; background: var(--gold); border: 6px solid #fff;
    display: flex; align-items: center; justify-content: center; text-align: center;
    font-weight: 700; font-size: 25px; line-height: 1.2; color: var(--ink);
  }

  .offer { color: var(--ink); }
  .qualify {
    position: absolute; left: 24px; top: 592px;
    font-weight: 700; font-size: 24px; line-height: 32px; letter-spacing: 0.2px; white-space: nowrap;
  }
  .qualify .highlight { color: var(--sky); }
  .perks { position: absolute; left: 24px; top: 628px; list-style: none; }
  .perks li { display: flex; align-items: center; gap: 10px; font-weight: 700; font-size: 22px; height: 30px; }
  .perks svg { width: 22px; height: 22px; flex: none; }
  .explainer {
    position: absolute; left: 24px; top: 716px; width: 700px;
    font-size: 21.5px; line-height: 26px; font-weight: 400;
  }

  .footer-panel { position: absolute; left: 0; top: 740px; width: 732px; height: 212px; }
  .fund-line {
    position: absolute; right: 18px; top: 852px;
    font-size: 26px; line-height: 34px; color: #fff; white-space: nowrap;
  }
  .fund-line strong { font-weight: 700; border-bottom: 2px solid var(--gold); padding-bottom: 3px; }
  .apply-line {
    position: absolute; right: 18px; top: 898px;
    font-weight: 700; font-size: 25px; line-height: 30px; color: var(--gold); letter-spacing: 0.3px; white-space: nowrap;
  }

  .contact-bar { position: absolute; left: 0; top: 954px; width: 732px; height: 82px; }
  .contact-shapes { position: absolute; left: 0; top: 0; }
  .phone { position: absolute; left: 30px; top: 0; height: 82px; display: flex; align-items: center; gap: 10px; }
  .phone svg { width: 36px; height: 36px; }
  .phone-number, .web-address {
    font-family: "Oswald", "Arial Narrow", sans-serif; font-weight: 500; letter-spacing: 0.2px; white-space: nowrap;
  }
  .phone-number { font-size: 33px; color: var(--brand-blue); }
  .globe { position: absolute; left: 385px; top: 23px; width: 36px; height: 36px; }
  .web-address {
    position: absolute; left: 462px; top: 0; width: 256px; height: 82px;
    display: flex; align-items: center; justify-content: center;
    font-size: 24px; color: var(--navy);
  }
</style>
</head>
<body>
  <main class="flyer">
    <div class="hero-photo" role="img" aria-label="Businessman in a suit touching a floating dollar sign, with a network of connected icons and warm blurred city lights behind him"></div>

    <svg class="logo-band" viewBox="0 0 444 96" aria-hidden="true">
      <polygon points="0,0 444,0 416,82 0,82" fill="#fff"/>
      <polygon points="0,82 416,82 410,96 0,96" fill="rgba(255,255,255,0.55)"/>
    </svg>
    <div class="logo">PELLARCAPITAL</div>

    <section class="headline-band">
      <h1 class="headline">NEED BUSINESS CAPITAL?</h1>
    </section>

    <div class="badge">NOT A<br>BUSINESS<br>LOAN</div>

    <section class="offer">
      <p class="qualify">YOU CAN QUALIFY FOR <span class="highlight">UP TO 500,000</span> IN JUST 24 HOURS</p>
      <ul class="perks">
        <li><svg viewBox="0 0 20 20"><path d="M2 11 L7 16 L18 3" fill="none" stroke="#f5c12e" stroke-width="2.6" stroke-linecap="round" stroke-linejoin="round"/></svg>No minimum credit score</li>
        <li><svg viewBox="0 0 20 20"><path d="M2 11 L7 16 L18 3" fill="none" stroke="#f5c12e" stroke-width="2.6" stroke-linecap="round" stroke-linejoin="round"/></svg>Simple 1 page application</li>
      </ul>
      <p class="explainer">Not a business loan, get a cash advance today on your future sales.<br>Convenient alternative to a bank loan.</p>
    </section>

    <svg class="footer-panel" viewBox="0 0 732 212" aria-hidden="true">
      <defs>
        <linearGradient id="panelShade" x1="0" y1="0" x2="1" y2="0">
          <stop offset="0" stop-color="#22338a"/>
          <stop offset="1" stop-color="#1c2b74"/>
        </linearGradient>
      </defs>
      <polygon points="0,130 732,4 732,212 0,212" fill="url(#panelShade)"/>
    </svg>
    <p class="fund-line">We fund virtually <strong>every type of business.</strong></p>
    <p class="apply-line">APPLY IN MINUTES ONLINE AT:</p>

    <div class="contact-bar">
      <svg class="contact-shapes" width="732" height="82" viewBox="0 0 732 82" aria-hidden="true">
        <polygon points="372,0 458,0 434,82 348,82" fill="var(--navy)"/>
        <polygon points="458,0 732,0 732,82 434,82" fill="var(--gold)"/>
      </svg>
      <div class="phone">
        <svg viewBox="0 0 36 36" aria-hidden="true">
          <path d="M9 4 L14 4 L16 11 L12.5 14 C14.5 18.5 17.5 21.5 22 23.5 L25 20 L32 22 L32 27 C32 30 29.5 32 27 31.5 C15 29.5 6.5 21 4.5 9 C4 6.5 6 4 9 4 Z" fill="var(--brand-blue)"/>
          <path d="M21 4 A11 11 0 0 1 32 15 M21 9 A6 6 0 0 1 27 15" fill="none" stroke="var(--brand-blue)" stroke-width="2.4" stroke-linecap="round"/>
        </svg>
        <span class="phone-number">1-800-GRAB-NOW</span>
      </div>
      <svg class="globe" viewBox="0 0 36 36" aria-hidden="true">
        <g fill="none" stroke="#fff" stroke-width="2.2">
          <circle cx="18" cy="18" r="14"/>
          <ellipse cx="18" cy="18" rx="6" ry="14"/>
          <line x1="4" y1="18" x2="32" y2="18"/>
          <path d="M7 10 H29 M7 26 H29"/>
        </g>
      </svg>
      <div class="web-address">PELLARCAPITAL.EXAMPLE</div>
    </div>
  </main>
</body>
</html>
```